Looking for a clean, modern, and professional business card design that reflects Valtrim Systems

The design should include the company logo, contact details, and align with our brand identity. Please use a sophisticated and minimalist style, incorporating [specific colors, if applicable]. Creativity is welcome, but the card must maintain a polished and professional appearance.

Details to Include:

Name: Gavin Trelowe
Title: VP Sales / Operations
Company: Valtrim Systems
Phone: 483.216.7705
Email: gavin@valtrimsystems-example.com
Website: www.valtrimsystems-example.com

```html
<!DOCTYPE html>
<html lang="en">
<head>
<meta charset="utf-8">
<title>Valtrim Systems – Business Card</title>
<link href="https://fonts.googleapis.com/css2?family=Montserrat:wght@400;600;700&family=Roboto:wght@400&display=swap" rel="stylesheet">
<style>
  :root{
    --bg:#e9eaec;
    --ink:#0d0d0f;
    --card-black:#151517;
    --paper:#ffffff;
    --brand-blue:#3b7fcf;
    --steel:#b9bcc0;
    --text-grey:#3a3a3a;
    --divider:#2f3a33;
  }
  *{box-sizing:border-box;margin:0;padding:0}
  html,body{width:1200px;height:800px;overflow:hidden;background:var(--bg)}
  .canvas{width:1200px;height:800px;display:flex;align-items:center;justify-content:center;gap:60px}
  .card{width:525px;height:300px;border-radius:22px;position:relative;overflow:hidden;box-shadow:0 10px 30px rgba(0,0,0,.18)}

  /* front */
  .card-front{background:var(--card-black);display:flex;align-items:center;justify-content:center}
  .wordmark{display:flex;align-items:center;gap:14px;font-family:'Montserrat',sans-serif;font-weight:700;letter-spacing:.08em;text-transform:uppercase}
  .wordmark-mark{width:18px;height:18px;background:var(--brand-blue)}
  .card-front .wordmark-name{color:var(--steel);font-size:36px}

  /* back */
  .card-back{background:var(--paper)}
  .back-main{position:absolute;left:0;top:0;right:0;height:232px;display:flex;align-items:center}
  .back-logo{width:225px;display:flex;justify-content:center}
  .card-back .wordmark{gap:8px}
  .card-back .wordmark-mark{width:11px;height:11px}
  .card-back .wordmark-name{color:var(--ink);font-size:19px}
  .back-divider{width:1px;height:150px;background:linear-gradient(var(--paper),var(--divider),var(--paper))}
  .contact{padding-left:26px}
  .person-name{font-family:'Montserrat',sans-serif;font-weight:700;font-size:19px;color:var(--ink);text-transform:uppercase;letter-spacing:.02em}
  .person-title{font-family:'Roboto',sans-serif;font-size:15px;color:var(--brand-blue);margin-top:2px;margin-bottom:16px}
  .contact-list{list-style:none;font-family:'Roboto',sans-serif;font-size:13px;color:var(--text-grey)}
  .contact-list li{display:flex;align-items:center;gap:9px;margin-top:6px}
  .contact-icon{width:15px;height:15px;flex:none}
  .back-band{position:absolute;left:0;right:0;bottom:0;height:68px;background:var(--ink);border-top:2px solid var(--brand-blue);box-shadow:inset 0 4px 0 var(--paper);display:flex;align-items:center;justify-content:center}
  .band-name{font-family:'Montserrat',sans-serif;font-weight:400;font-size:14px;letter-spacing:.32em;color:var(--paper);text-transform:uppercase}
</style>
</head>
<body>
<main class="canvas">
  <section class="card card-front" aria-label="Card front">
    <div class="wordmark">
      <span class="wordmark-mark"></span>
      <span class="wordmark-name">Valtrim Systems</span>
    </div>
  </section>

  <section class="card card-back" aria-label="Card back">
    <div class="back-main">
      <div class="back-logo">
        <div class="wordmark">
          <span class="wordmark-mark"></span>
          <span class="wordmark-name">Valtrim Systems</span>
        </div>
      </div>
      <div class="back-divider"></div>
      <div class="contact">
        <h1 class="person-name">Gavin Trelowe</h1>
        <p class="person-title">VP Sales / Operations</p>
        <ul class="contact-list">
          <li>
            <svg class="contact-icon" viewBox="0 0 16 16"><circle cx="8" cy="8" r="8" fill="#3b7fcf"/><path d="M5 4.5c.6-.4 1.2-.3 1.5.3l.6 1.2c.2.4 0 .8-.3 1l-.5.4c.4.9 1.1 1.6 2 2l.4-.5c.3-.3.7-.4 1-.2l1.2.6c.6.3.7.9.3 1.5-.6.9-1.6 1.1-2.6.6C6.7 10.4 5.6 9.3 4.6 7.5 4.1 6.3 4.2 5.2 5 4.5z" fill="#fff"/></svg>
            <span>483.216.7705</span>
          </li>
          <li>
            <svg class="contact-icon" viewBox="0 0 16 16"><circle cx="8" cy="8" r="8" fill="#3b7fcf"/><rect x="4" y="5" width="8" height="6" rx="1" fill="#fff"/><path d="M4.3 5.4 8 8.3l3.7-2.9" fill="none" stroke="#3b7fcf" stroke-width="1"/></svg>
            <span>gavin@valtrimsystems-example.com</span>
          </li>
          <li>
            <svg class="contact-icon" viewBox="0 0 16 16"><circle cx="8" cy="8" r="8" fill="#3b7fcf"/><circle cx="8" cy="8" r="4.2" fill="none" stroke="#fff" stroke-width="1"/><ellipse cx="8" cy="8" rx="1.8" ry="4.2" fill="none" stroke="#fff" stroke-width="1"/><path d="M3.8 8h8.4" stroke="#fff" stroke-width="1"/></svg>
            <span>www.valtrimsystems-example.com</span>
          </li>
        </ul>
      </div>
    </div>
    <div class="back-band">
      <span class="band-name">Valtrim Systems</span>
    </div>
  </section>
</main>
</body>
</html>
```